Marks of Dunmore business card design

I need a clean, professional looking design using the attached logo with a bright green/ gray/dark gray/black colors. Maybe even an orange accent if it looks good. I am open to slight changes in the logo if needed. Details below on the info on what should be on the cards. We are a sign company in Ft. Lauderdale FL that specializes in yacht lettering on multi million dollar yachts.

Target Market(s)

marine industry, yachts

Industry/Entity Type

Business

Colors
9bcb3c
000000
606060
f37122

Requirements
Must have
• address: 4837 W. Tallow Rd.
• Coral Haven, FL 33071
• Phone: 954-518-4062
• email/website: marksofdunmore@postvane.com MarksofDunmore.com
Nice to have
• I would like it very clean and simple but professional looking. Nice layout and would prefer a darker background. Orange highlight only if it works.
Should not have
• Nothing fancy.

```html
<!DOCTYPE html>
<html lang="en">
<head>
<meta charset="utf-8">
<title>Marks of Dunmore – Business Card</title>
<link rel="stylesheet" href="https://fonts.googleapis.com/css2?family=Open+Sans:ital,wght@0,400;0,700;0,800;1,700&display=swap">
<style>
  :root {
    --stage: #363636;
    --card-dark: #121212;
    --brand-green: #02963f;
    --accent-orange: #f37122;
    --text-light: #ffffff;
    --text-soft: #e6e6e6;
  }
  * { box-sizing: border-box; margin: 0; padding: 0; }
  html, body { width: 1200px; height: 900px; overflow: hidden; }
  body {
    background: var(--stage);
    font-family: "Open Sans", Arial, sans-serif;
    position: relative;
  }
  .card {
    position: absolute;
    top: 306px;
    height: 271px;
    overflow: hidden;
  }
  .card--front { left: 149px; width: 439px; background: var(--card-dark); }
  .card--back { left: 608px; width: 441px; background: var(--brand-green); }

  .name-tab { position: absolute; left: 0; top: 26px; width: 29px; height: 37px; }
  .holder { position: absolute; left: 38px; top: 30px; }
  .holder__name {
    color: var(--brand-green);
    font-weight: 700;
    font-style: italic;
    font-variant: small-caps;
    font-size: 17px;
    line-height: 20px;
    letter-spacing: 0.2px;
  }
  .holder__title { color: var(--text-soft); font-size: 12px; line-height: 14px; }

  .wordmark {
    position: absolute;
    font-weight: 800;
    text-transform: uppercase;
    white-space: nowrap;
    letter-spacing: 0.5px;
  }
  .wordmark--front { right: 25px; top: 106px; color: var(--brand-green); font-size: 20px; }
  .wordmark--back {
    left: 0; right: 0; top: 119px; text-align: center;
    color: var(--text-light); font-size: 28px;
  }

  .contact { position: absolute; left: 24px; top: 186px; list-style: none; }
  .contact li {
    display: flex; align-items: center; gap: 5px;
    color: var(--text-soft); font-size: 12px; line-height: 16px;
  }
  .contact svg { width: 10px; height: 10px; fill: var(--brand-green); }

  .address {
    position: absolute; right: 23px; top: 205px; text-align: right;
    color: var(--text-soft); font-size: 12px; line-height: 16px; font-style: normal;
  }
  .footer-band { position: absolute; left: 0; bottom: 0; width: 439px; height: 19px; }
</style>
</head>
<body>
  <section class="card card--front">
    <svg class="name-tab" viewBox="0 0 29 37" aria-hidden="true">
      <polygon points="0,0 12,0 16,37 0,37" fill="#02963f"/>
      <polygon points="13,0 29,0 29,37 17,37" fill="#f37122"/>
    </svg>
    <div class="holder">
      <p class="holder__name">Daniel Harlow</p>
      <p class="holder__title">Managing Director</p>
    </div>

    <p class="wordmark wordmark--front">Marks of Dunmore</p>

    <ul class="contact">
      <li><svg viewBox="0 0 10 10" aria-hidden="true"><path d="M2 0.5l2 2-1 1.3c.6 1.3 1.5 2.2 2.8 2.8l1.3-1 2 2-1.3 1.9C4 9.2.8 6 .3 1.8z"/></svg>954-518-4062</li>
      <li><svg viewBox="0 0 10 10" aria-hidden="true"><path d="M0 2h10v6H0z M0 2l5 3.3L10 2" stroke="#121212" stroke-width="0.8"/></svg>marksofdunmore@postvane.com</li>
      <li><svg viewBox="0 0 10 10" aria-hidden="true"><circle cx="5" cy="5" r="4.6"/><path d="M1 5h8M5 .5c-2 2.5-2 6.5 0 9M5 .5c2 2.5 2 6.5 0 9" stroke="#121212" stroke-width="0.7" fill="none"/></svg>www.MarksofDunmore.com</li>
    </ul>

    <address class="address">4837 W. Tallow Rd.<br>Coral Haven, FL 33071</address>

    <svg class="footer-band" viewBox="0 0 439 19" aria-hidden="true">
      <polygon points="0,0 218,0 204,19 0,19" fill="#02963f"/>
      <polygon points="224,0 439,0 439,19 208,19" fill="#f37122"/>
    </svg>
  </section>

  <section class="card card--back">
    <p class="wordmark wordmark--back">Marks of Dunmore</p>
  </section>
</body>
</html>
```